Etiketten-Design für Honigglas
Zielgruppe
Wir sind eine Imkerei; unsere Zielgruppe sind Privatpersonen welche Freude am exklusiven Naturprodukt Honig haben.
Aufgabenstellung
Format:
Etikett für 250-gr.-Honigglas (TO ∅ 63 mm).
Standardmaßgrösse 165 × 40 mm
Design:
schlicht, hochwertig, modern, edel/royal, unkonventionelles Design (weg von Bienen, Waben, Landschaften usw.), dunkle Farbtöne in Kontrast zu heller Schrift, die beiden Textbausteine 'Los Nr. ' sowie 'Haltbarkeit' (siehe unten) müssen von Hand leserlich beschriftbar sein.
Inhalt (Textangaben Pflicht):
- 250 g netto
- Honig gut verschlossen, kühl (max. 15°C), dunkel und trocken lagern. Kandierten Honig nicht über 40°C erwärmen.
- Mattenwiler Bienenhonig
- Los Nr.:
- Mind. haltbar bis Ende:

```html
<!DOCTYPE html>
<html lang="de">
<head>
<meta charset="utf-8">
<title>Mattenwiler Bienenhonig – Etikettenvarianten</title>
<link href="https://fonts.googleapis.com/css2?family=Comfortaa:wght@500&family=Lato:wght@400&display=swap" rel="stylesheet">
<style>
  :root {
    --ink: #050505;
    --paper: #ffffff;
    --gold-dark: #b8902a;
    --gold-light: #f7d27a;
    --grey-dark: #1f1f1f;
    --grey-mid: #5a5a5a;
    --grey-light: #787878;
  }
  html, body { margin: 0; padding: 0; overflow: hidden; }
  body { width: 1200px; height: 646px; background: var(--paper); position: relative; }

  .label {
    position: absolute; left: 0; width: 1198px; height: 314px;
    border: 1px solid var(--ink); overflow: hidden;
    font-family: "Lato", sans-serif; color: var(--paper);
  }
  .label--dark { top: 0; background: linear-gradient(90deg, var(--grey-dark) 0%, #3a3a3a 30%, var(--grey-light) 65%, #6a6a6a 100%); }
  .label--gold { top: 330px; background: linear-gradient(90deg, #111 0%, var(--grey-mid) 30%, #2a2a2a 55%, #0b0b0b 100%); }

  .write-field { position: absolute; left: 22px; width: 26px; background: var(--paper); }
  .write-field--date { top: 15px; height: 63px; }
  .write-field--lot { top: 209px; height: 49px; }

  .vertical { position: absolute; white-space: nowrap; transform: rotate(-90deg); transform-origin: left top; font-size: 11px; }
  .field-label--date { left: 25px; top: 202px; }
  .field-label--lot { left: 25px; top: 300px; }

  .net-weight { position: absolute; left: 56px; top: 290px; font-size: 11px; }

  .art { position: absolute; left: 0; top: 0; }

  .title {
    position: absolute; left: 508px; top: 78px; margin: 0;
    font-family: "Comfortaa", sans-serif; font-weight: 500;
    font-size: 48px; line-height: 60px; letter-spacing: 1px;
  }
  .label--dark .title { color: var(--gold-light); background: linear-gradient(90deg, var(--gold-dark), var(--gold-light) 60%, var(--gold-dark)); -webkit-background-clip: text; background-clip: text; -webkit-text-fill-color: transparent; }
  .label--gold .title { color: var(--ink); left: 512px; top: 82px; }
  .title span { display: block; }

  .storage {
    position: absolute; left: 1108px; top: 298px;
    transform: rotate(-90deg); transform-origin: left top;
    font-size: 10.5px; line-height: 14.5px; width: 290px; margin: 0;
  }
</style>
</head>
<body>

<section class="label label--dark">
  <div class="write-field write-field--date"></div>
  <div class="write-field write-field--lot"></div>
  <span class="vertical field-label--date">Mind. haltbar bis Ende:</span>
  <span class="vertical field-label--lot">Los Nr.:</span>
  <span class="net-weight">250 g netto</span>

  <svg class="art" width="1198" height="314" viewBox="0 0 1198 314">
    <defs>
      <linearGradient id="goldLine" x1="0" x2="1"><stop offset="0" stop-color="#b8902a"/><stop offset="0.6" stop-color="#f0c85e"/><stop offset="1" stop-color="#b8902a"/></linearGradient>
    </defs>
    <rect x="366" y="43" width="482" height="225" fill="none" stroke="url(#goldLine)" stroke-width="3"/>
    <path role="img" aria-label="Schwarzer Pinselstrich mit Farbspritzern hinter dem Produktnamen"
      d="M330 130 L380 100 L470 90 L540 78 L700 80 L876 72 L878 120 L860 150 L875 190 L868 262 L890 272 L800 285 L650 282 L520 290 L420 270 L360 250 L335 210 L322 170 Z"
      fill="var(--ink)"/>
  </svg>

  <h1 class="title"><span>mattenwiler</span><span>bienenhonig</span></h1>

  <p class="storage">Imkerei Brunner &amp; Liechti, 8847 Mattenwil<br>Mühlegasse 12, kolmar7@postfach.ch,<br>Honig gut verschlossen, kühl (max. 15°C), dunkel und<br>trocken lagern. Kandierten Honig nicht über 40°C<br>erwärmen.</p>
</section>

<section class="label label--gold">
  <div class="write-field write-field--date"></div>
  <div class="write-field write-field--lot"></div>
  <span class="vertical field-label--date">Mind. haltbar bis Ende:</span>
  <span class="vertical field-label--lot">Los Nr.:</span>
  <span class="net-weight">250 g netto</span>

  <svg class="art" width="1198" height="314" viewBox="0 0 1198 314">
    <defs>
      <linearGradient id="goldBrush" x1="0" x2="1"><stop offset="0" stop-color="#a8821f"/><stop offset="0.35" stop-color="#c99a35"/><stop offset="0.65" stop-color="#f9d67a"/><stop offset="1" stop-color="#c4982e"/></linearGradient>
    </defs>
    <rect x="338" y="32" width="484" height="227" fill="none" stroke="var(--paper)" stroke-width="3"/>
    <path role="img" aria-label="Goldener Pinselstrich mit Farbspritzern hinter dem Produktnamen"
      d="M250 190 L300 160 L330 110 L380 90 L420 60 L520 50 L650 45 L872 40 L870 120 L880 160 L870 230 L890 255 L800 270 L680 262 L520 258 L400 262 L320 250 L260 230 Z"
      fill="url(#goldBrush)"/>
  </svg>

  <h1 class="title"><span>mattenwiler</span><span>bienenhonig</span></h1>

  <p class="storage">Imkerei Brunner &amp; Liechti, 8847 Mattenwil<br>Mühlegasse 12, kolmar7@postfach.ch,<br>Honig gut verschlossen, kühl (max. 15°C), dunkel und<br>trocken lagern. Kandierten Honig nicht über 40°C<br>erwärmen.</p>
</section>

</body>
</html>
```